Office Suite Inspection Report

We are building a certification program for rent-able office space
And we need a document that we can supply as an inspection report.
This document, in most scenarios, is going to be co-branded with the landlord and is something that they can give their clients so that they fully understand the expected expenses that will be incurred by renting that location and will serve as an introduction to our company as a trusted provider of the types of services you need to run a modern cloud connected office.
We are working with landlords whom will provide us with the basic details of each of their rent-able office spaces so that we can outline the suitability of the space for networking services.
Document Outline
Desk Harbor Logo
Picture Of the rental space
Opening Text
Available Connectivity Options (
this should be a horizontal table of 3 to 4 options with the providers logo and 3-4 word description of the service and the price estimate )
Site Physical Inspection, this should be images and text about specific items of notice such as if there is a networking closet or room
We then want to offer pricing options for our services based on the expected number of users the office space should support
I have attached a presentation with a number of our services listed.
The following services are priced on a per user basis
Office / Productivity
Email
VoIP (Telephone Services)
Remote File Access
The following services are priced by location
Remote Backup
Network Services ( wired / wireless )
Ideally we can fit this on 2 - 3 pages
Connectivity Providers Logos -
Meridian Wave
https://www.findpix-example.test/search?q=meridian+wave+logo
Pell
https://www.findpix-example.test/search?q=pell+logo
Orvanet
https://www.findpix-example.test/search?q=pell+logo#q=qtnet+logo

```html
<!DOCTYPE html>
<html lang="en">
<head>
<meta charset="utf-8">
<title>Desk Harbor – Office Suite Inspection Report</title>
<link rel="stylesheet" href="https://fonts.googleapis.com/css2?family=Nunito:wght@700;800&family=Open+Sans:wght@400;600;700&display=swap">
<style>
  :root{
    --canvas:#e6e7e9;
    --paper:#ffffff;
    --sky:#b5e0f6;
    --navy:#1b3765;
    --blue:#2f8fd6;
    --ink:#23436f;
    --muted:#3d5a80;
  }
  *{box-sizing:border-box;margin:0;padding:0}
  html,body{width:1200px;height:1200px;overflow:hidden}
  body{background:var(--canvas);font-family:"Open Sans",Arial,sans-serif;color:var(--ink);position:relative}

  .page{position:absolute;width:680px;height:420px;background:var(--paper);overflow:hidden;border:1px solid #d3d6da}
  .page--cover{left:70px;top:60px}
  .page--inspection{left:450px;top:380px}
  .page--pricing{left:110px;top:750px}

  .page__body{position:absolute;left:0;right:0;top:72px;height:310px;background:linear-gradient(180deg,var(--sky) 0%,var(--sky) 70%,#d5eefa 100%)}
  .page__stripe{position:absolute;left:0;right:0;top:378px;height:6px;
    background:linear-gradient(90deg,var(--navy) 0 16%,var(--blue) 16% 33%,var(--navy) 33% 50%,var(--blue) 50% 66%,var(--navy) 66% 83%,var(--blue) 83% 100%)}

  .brand{position:absolute;left:40px;top:18px;display:flex;align-items:center;gap:10px}
  .brand__dot{width:30px;height:30px;border-radius:50%;background:var(--blue)}
  .brand__name{font-family:"Nunito",Arial,sans-serif;font-weight:800;font-size:28px;color:var(--navy);letter-spacing:-.3px}

  .visual{position:absolute;border-radius:8px}
  .visual--city{left:40px;top:100px;width:400px;height:240px;border-radius:0;background:radial-gradient(ellipse at 50% 60%,#6fa9da 0%,#9ccbee 55%,rgba(181,224,246,0) 80%)}
  .visual--meeting{left:478px;top:100px;width:170px;height:115px;border:3px solid #f1d99a;background:linear-gradient(160deg,#f4f4f2,#d8d4cb 70%,#b99a6c)}
  .visual--building{left:490px;top:225px;width:165px;height:115px;background:linear-gradient(180deg,#6ea2d6 0%,#a9c8e4 45%,#dfe3e6 60%,#8c9299 100%)}

  .section-title{position:absolute;font-family:"Nunito",Arial,sans-serif;font-weight:800;color:var(--navy)}
  .page--inspection .section-title{left:45px;top:88px;font-size:20px}
  .visual--training{left:45px;top:122px;width:355px;height:248px;border-radius:12px;background:linear-gradient(180deg,#e8ecee 0%,#cfd5d8 45%,#6d5a48 70%,#3b3a3c 100%)}

  .provider{position:absolute;background:#fff;width:112px;height:78px;padding:8px 7px 7px;border-radius:3px}
  .provider--meridian{left:410px;top:112px}
  .provider--orvanet{left:540px;top:104px}
  .provider--pell{left:545px;top:190px}
  .provider__name{display:block;font-family:"Nunito",Arial,sans-serif;font-weight:800;font-size:13px;color:var(--blue);text-align:center;margin-bottom:5px;white-space:nowrap}
  .provider__note{font-size:7px;line-height:1.4;color:var(--ink);text-align:center}
  .site-note{position:absolute;left:418px;top:218px;font-family:"Nunito",Arial,sans-serif;font-weight:700;font-size:13px;line-height:1.2;color:var(--navy)}

  .pricing-intro{position:absolute;left:45px;top:86px;font-size:11.5px;font-weight:700;color:var(--navy);text-transform:uppercase;letter-spacing:.2px}
  .service{position:absolute;background:#fff;width:300px;height:128px;padding:10px 12px}
  .service--productivity{left:40px;top:110px}
  .service--voip{left:350px;top:100px}
  .service--email{left:40px;top:248px}
  .service--files{left:350px;top:238px}
  .service__name{font-family:"Nunito",Arial,sans-serif;font-weight:800;font-size:13px;color:var(--navy);text-transform:uppercase;margin-bottom:4px}
  .service__tiers{display:flex;gap:10px}
  .tier{flex:1;position:relative;height:88px}
  .tier__label{font-size:7.5px;font-weight:700;color:var(--navy);text-transform:uppercase;margin-bottom:2px}
  .tier__list{list-style:none;font-size:6.5px;line-height:1.4;color:var(--muted)}
  .tier__list li::before{content:"• "}
  .tier__price{position:absolute;left:0;bottom:0;background:var(--navy);color:#fff;font-weight:700;font-size:11px;padding:2px 7px}
</style>
</head>
<body>

<section class="page page--cover">
  <div class="brand"><span class="brand__dot"></span><span class="brand__name">DeskHarbor.io</span></div>
  <div class="page__body"></div>
  <div class="visual visual--city" role="img" aria-label="Blue 3D illustration of a city block of office towers"></div>
  <div class="visual visual--meeting" role="img" aria-label="Photo of a bright empty conference room with white chairs"></div>
  <div class="visual visual--building" role="img" aria-label="Photo of a modern glass office building under a blue sky"></div>
  <div class="page__stripe"></div>
</section>

<section class="page page--inspection">
  <div class="brand"><span class="brand__dot"></span><span class="brand__name">DeskHarbor.io</span></div>
  <div class="page__body"></div>
  <h2 class="section-title">Site Physical Inspection</h2>
  <div class="visual visual--training" role="img" aria-label="Photo of a training room with people seated at desks facing a projection screen"></div>
  <div class="provider provider--meridian"><span class="provider__name">Meridian Wave</span><p class="provider__note">Business fiber service, 100 Mbps, est. $85/mo</p></div>
  <div class="provider provider--orvanet"><span class="provider__name">Orvanet</span><p class="provider__note">Cable broadband, 50 Mbps plus, est. $70/mo</p></div>
  <div class="provider provider--pell"><span class="provider__name">Pell</span><p class="provider__note">Metro ethernet, dedicated line, est. $120/mo</p></div>
  <p class="site-note">networking closet<br>or room</p>
  <div class="page__stripe"></div>
</section>

<section class="page page--pricing">
  <div class="brand"><span class="brand__dot"></span><span class="brand__name">DeskHarbor.io</span></div>
  <div class="page__body"></div>
  <h2 class="pricing-intro">The following services are priced on a per user basis:</h2>

  <article class="service service--productivity">
    <h3 class="service__name">Productivity</h3>
    <div class="service__tiers">
      <div class="tier"><p class="tier__label">Standard</p>
        <ul class="tier__list"><li>Northvale Office Suite Licensing</li><li>Application installation and updates</li></ul>
        <span class="tier__price">$15.00</span></div>
      <div class="tier"><p class="tier__label">Power Users</p>
        <ul class="tier__list"><li>All the features of Productivity - Standard</li><li>Additional 20+ Business-class Applications</li><li>Web, Utilities, Messaging, Media, Runtimes, Compression, Imaging, Documents, Security, Tools, Online Storage</li></ul>
        <span class="tier__price">$30.00</span></div>
    </div>
  </article>

  <article class="service service--voip">
    <h3 class="service__name">VoIP</h3>
    <div class="service__tiers">
      <div class="tier"><p class="tier__label">Standard</p>
        <ul class="tier__list"><li>Business-class phone service with unlimited calling</li><li>Includes 30+ features</li><li>Extended mobility features</li></ul>
        <span class="tier__price">$25.00</span></div>
      <div class="tier"><p class="tier__label">Power Users</p>
        <ul class="tier__list"><li>All the features of User - Standard</li><li>Call Recording • Personal Fax box</li><li>Personal Music On hold</li><li>Personal Conference Bridge</li></ul>
        <span class="tier__price">$30.00</span></div>
    </div>
  </article>

  <article class="service service--email">
    <h3 class="service__name">Email</h3>
    <div class="service__tiers">
      <div class="tier"><p class="tier__label">Standard</p>
        <ul class="tier__list"><li>Business-class email with 50 GB mailbox</li><li>SPAM filtering and virus protection</li><li>Mailcraft and mobile device support</li><li>Administration of users and email server</li></ul>
        <span class="tier__price">$15.00</span></div>
      <div class="tier"><p class="tier__label">Power Users</p>
        <ul class="tier__list"><li>All the features of Email - Standard</li><li>Unlimited email storage for in-place archive</li><li>Archiving and legal hold</li></ul>
        <span class="tier__price">$30.00</span></div>
    </div>
  </article>

  <article class="service service--files">
    <h3 class="service__name">File Sharing &amp; Cloud Access</h3>
    <div class="service__tiers">
      <div class="tier"><p class="tier__label">Standard</p>
        <ul class="tier__list"><li>Business-class file sharing with real time cloud sync*</li><li>Automatic file versioning</li><li>Define user permissions for each share</li><li>Administration of users and site storage appliance site</li></ul>
        <span class="tier__price">$15.00</span></div>
      <div class="tier"><p class="tier__label">Power Users</p>
        <ul class="tier__list"><li>All the features of File Sharing - Standard</li><li>Access shares anywhere via network drives</li></ul>
        <span class="tier__price">$30.00</span></div>
    </div>
  </article>

  <div class="page__stripe"></div>
</section>

</body>
</html>
```